Gedric's Lager BEER CAN

DESIGN USE
This is not for a business, it's for a (thoughtful) gift to my father. The design is going to be on a personalised beer can, so it will be a cylindrical shape. Basically, I'm giving him a few six-packs with his own beer label. I've attached the copy and put design specs below.
RATIONALE
My Dad is a cool guy, one of life’s absolute gems. He’s not a big drinker, but he likes a beer and he’s more likely to give them away at Christmas time than keep them in the fridge and drink them himself.
He’s also a master of Dad Jokes and offering pearls of wisdom, so combining a good beer with a funny Dad Joke or two on a can will be a great gift to give him for his birthday, Father’s Day or Christmas.
PLACEMENT
The front of the can needs to be my Dad’s head in cartoon form and GEDRIC’S LAGER has to be the most prominent wording.
While GEDRIC’S LAGER is the main heading…I’d like A TAMSWORTH RISE BREW up the top and GEDRIC’S LAGER IS LIFE’S BEER NECESSITY as the key wording wrapping around the bottom of the can.
I'd also like these sayings/jokes included (all of them OR as many that look cool and don't make the design too crowded):
“A beer in each hand is a balanced diet,” - Gedric

“This beer tastes like I’m not going to work tomorrow,” - Gedric

“Your beer isn’t half-full…it’s halfway to your next brew,” - Gedric

“My doc says I shouldn’t drink every day…that’s why I tend to drink at night,” - Gedric

“Two beer or not two beer,” - Shakesbeer

Why do frogs taste like beer?
Because of all the hops

What does Santa Claus drink?
A polar beer
Why do we like beer?
Coz you can’t drink bacon

Fat? Nah, beer makes you lean…
…against walls, doors…hotties

What's a beer’s favourite language?
Hebrew
DESIGN
Use the photos as a guide to turn my Dad (Gedric) into a cartoon - smiling/grinning, upbeat and happy. Not too old looking!
In terms of the can’s design, this is where I want YOU to be a design maestro. His head could burst through GEDRIC’S LAGER or simply have the lettering wrapped around his image.
Are the quotes and jokes in speech bubbles? Or are they in beer bubbles? Is a smaller version of Dad’s head used as a bullet point by each quote or joke?
FONT
Your choice! It just needs to be easy to read or and not too old-fashioned or - at the other extreme - too futuristic.
COLOUR
Your choice! He’s from a province that has red and black as their core colours, but if that doesn’t work, please go with a light teal/blue - or some other semi-masculine colour - and a dark colouring for the wording/lettering.
FORMAT
The approved copy needs to be provided as a PDF and a jpeg.
Maximum size is 250 MB
DIMENSIONS
160mm wide by 85mm high.

Target Market(s)

A target market of ONE - my Dad. I want him to LOVE his gift - his own personal beer can with his image and name on it.

Industry/Entity Type

Beer...

Colors

Designer to choose colors to be used in the design.

Requirements
Must have
• A fun, impactful BEER CAN design featuring my Dad's cartoon visage and some if not all of the Dad Jokes/beer sayings provided.

```html
<!DOCTYPE html>
<html lang="en">
<head>
<meta charset="utf-8">
<title>Gedric's Lager – Can Label Options</title>
<link rel="stylesheet" href="https://fonts.googleapis.com/css2?family=Quicksand:wght@600;700&display=swap">
<style>
  :root {
    --paper: #ffffff;
    --navy-deep: #17183a;
    --navy-mid: #1d3770;
    --blue-bright: #1f559c;
    --gold: #f5b22a;
    --white: #ffffff;
    --pattern-tone: #6f7390;
    --paisley-tone: #2f5fa6;
    --portrait-light: #8a8f9b;
    --portrait-dark: #2e3440;
  }
  * { box-sizing: border-box; margin: 0; padding: 0; }
  html, body {
    width: 712px; height: 1200px; overflow: hidden;
    background: var(--paper);
    font-family: "Quicksand", sans-serif;
  }
  .label {
    position: absolute; left: 44px; width: 623px; height: 331px;
    overflow: hidden; color: var(--white);
    background: linear-gradient(180deg, var(--navy-deep) 0%, var(--navy-mid) 55%, var(--blue-bright) 100%);
  }
  .label--one { top: 67px; }
  .label--two { top: 436px; }
  .label--three {
    top: 804px;
    background: linear-gradient(180deg, var(--blue-bright) 0%, var(--navy-mid) 50%, var(--navy-deep) 100%);
  }
  .pattern-band {
    position: absolute; left: 0; top: 0; width: 100%; height: 48px;
    background: linear-gradient(180deg, var(--pattern-tone) 0%, rgba(111,115,144,0.35) 100%);
  }
  .paisley-field {
    position: absolute; left: 0; top: 0; width: 100%; height: 210px;
    background: linear-gradient(180deg, var(--paisley-tone) 0%, rgba(47,95,166,0) 100%);
  }
  .brand-name {
    position: absolute; left: 219px; top: 58px; width: 184px; height: 40px;
    font-weight: 700; font-size: 25px;
    line-height: 40px; text-align: center; color: var(--white); white-space: nowrap;
  }
  .crest { position: absolute; left: 225px; top: 98px; width: 172px; height: 166px; }
  .tagline {
    position: absolute; left: 0; top: 296px; width: 100%;
    text-align: center; font-weight: 700; font-size: 23.5px; letter-spacing: 0.2px;
    color: var(--white); white-space: nowrap;
  }
  .label--three .tagline { color: var(--gold); }
  .bubble-lines { position: absolute; left: 0; top: 0; width: 623px; height: 331px; }
  .bubble-text {
    position: absolute; font-weight: 600; font-size: 9.2px; line-height: 11.2px;
    text-align: center; display: flex; align-items: center; justify-content: center;
    white-space: nowrap;
  }
  .joke-column {
    position: absolute; top: 59px; width: 154px; height: 231px;
    border: 1.5px solid var(--gold); border-radius: 16px;
    display: flex; flex-direction: column; justify-content: center; gap: 12px;
    font-weight: 600; font-size: 10.2px; line-height: 12.4px; text-align: center;
    white-space: nowrap;
  }
  .joke-column--sayings { left: 28px; }
  .joke-column--jokes { left: 441px; }
</style>
</head>
<body>

<section class="label label--one">
  <div class="pattern-band" role="img" aria-label="Woven geometric border pattern"></div>
  <div class="brand-name">GEDRIC’S LAGER</div>
  <svg class="crest" viewBox="0 0 172 166">
    <defs><radialGradient id="portrait1" cx="50%" cy="40%" r="55%"><stop offset="0" stop-color="var(--portrait-light)"/><stop offset="1" stop-color="var(--portrait-dark)"/></radialGradient></defs>
    <path d="M4 4 H168 V118 L86 164 L4 118 Z" fill="var(--gold)"/>
    <path d="M14 10 H158 V112 L86 152 L14 112 Z" fill="var(--blue-bright)"/>
    <rect x="24" y="14" width="124" height="126" fill="url(#portrait1)" role="img" aria-label="Cartoon portrait of Gedric, smiling, with glasses"/>
  </svg>
  <svg class="bubble-lines" viewBox="0 0 623 331" fill="none" stroke="var(--gold)" stroke-width="1.4" stroke-linejoin="round">
    <path d="M54.5,57.5 H154 Q170,57.5 170,73.5 V78 Q178,94 196,103 Q175,100 155,94 H54.5 Q38.5,94 38.5,78 V73.5 Q38.5,57.5 54.5,57.5 Z"/>
    <path d="M54.5,102 H154 Q170,102 170,118 V122 Q178,142 197,153 Q175,150 155,143.5 H54.5 Q38.5,143.5 38.5,127.5 V118 Q38.5,102 54.5,102 Z"/>
    <path d="M54.5,152 H154 Q170,152 170,168 V172 Q178,193 196,204 Q175,200 155,194 H54.5 Q38.5,194 38.5,178 V168 Q38.5,152 54.5,152 Z"/>
    <path d="M54.5,203 H154 Q170,203 170,217 V219 Q182,222 197,225 Q182,228 170,236 V240 Q170,256 154,256 H54.5 Q38.5,256 38.5,240 V219 Q38.5,203 54.5,203 Z"/>
    <path d="M52.5,263 H160 Q180,262 197,265 Q180,272 168,285 Q163,291 156,291 H52.5 Q38.5,291 38.5,277 Q38.5,263 52.5,263 Z"/>
    <path d="M459,59 H568 Q584,59 584,75 V98 Q584,114 568,114 H462 Q437,120 417,124 Q436,114 443,100 V75 Q443,59 459,59 Z"/>
    <path d="M459,124.5 H568 Q584,124.5 584,140.5 V153 Q584,169 568,169 H462 Q437,174 417,178 Q436,168 443,155 V140.5 Q443,124.5 459,124.5 Z"/>
    <path d="M459,179 H568 Q584,179 584,195 V209 Q584,225 568,225 H462 Q437,230 417,234 Q436,224 443,211 V195 Q443,179 459,179 Z"/>
    <path d="M459,235 H568 Q584,235 584,251 V275 Q584,291 568,291 H459 Q443,291 443,275 V264 Q430,262 417,258 Q432,254 443,248 Q443,235 459,235 Z"/>
  </svg>
  <div class="bubble-text" style="left:38.5px;top:57.5px;width:131.5px;height:36.5px">“A beer in each hand is a<br>balanced diet,” - Gedric</div>
  <div class="bubble-text" style="left:38.5px;top:102px;width:131.5px;height:41.5px">“This beer tastes like I’m<br>not going to work<br>tomorrow,” - Gedric</div>
  <div class="bubble-text" style="left:38.5px;top:152px;width:131.5px;height:42px">“Your beer isn’t<br>half-full…it’s halfway to<br>your next brew,” - Gedric</div>
  <div class="bubble-text" style="left:38.5px;top:203px;width:131.5px;height:53px">“My doc says I shouldn’t<br>drink every day…<br>that’s why I tend to drink<br>at night,” - Gedric</div>
  <div class="bubble-text" style="left:38.5px;top:263px;width:131.5px;height:28px">“Two beer or not two<br>beer,” - Shakesbeer</div>
  <div class="bubble-text" style="left:443px;top:59px;width:141px;height:55px">What does Santa Claus<br>drink? A polar beer<br>Why do we like beer?<br>Coz you can’t drink bacon</div>
  <div class="bubble-text" style="left:443px;top:124.5px;width:141px;height:44.5px">Why do frogs taste like<br>beer? Because of all the<br>hops</div>
  <div class="bubble-text" style="left:443px;top:179px;width:141px;height:46px">What's a beer’s favourite<br>language?<br>Hebrew</div>
  <div class="bubble-text" style="left:443px;top:235px;width:141px;height:56px">Fat? Nah, beer makes you<br>lean…<br>…against walls,<br>doors…hotties</div>
  <div class="tagline">GEDRIC’S LAGER IS LIFE’S BEER NECESSITY</div>
</section>

<section class="label label--two">
  <div class="pattern-band" role="img" aria-label="Woven geometric border pattern"></div>
  <div class="brand-name">GEDRIC’S LAGER</div>
  <svg class="crest" viewBox="0 0 172 166">
    <defs><radialGradient id="portrait2" cx="50%" cy="40%" r="55%"><stop offset="0" stop-color="var(--portrait-light)"/><stop offset="1" stop-color="var(--portrait-dark)"/></radialGradient></defs>
    <path d="M4 4 H168 V118 L86 164 L4 118 Z" fill="var(--gold)"/>
    <path d="M14 10 H158 V112 L86 152 L14 112 Z" fill="var(--blue-bright)"/>
    <rect x="24" y="14" width="124" height="126" fill="url(#portrait2)" role="img" aria-label="Cartoon portrait of Gedric, smiling, with glasses"/>
  </svg>
  <div class="joke-column joke-column--sayings">
    <p>“A beer in each hand is a<br>balanced diet,” - Gedric</p>
    <p>“This beer tastes like I’m<br>not going to work<br>tomorrow,” - Gedric</p>
    <p>“Your beer isn’t<br>half-full…it’s halfway to<br>your next brew,” - Gedric</p>
    <p>“My doc says I shouldn’t<br>drink every day…<br>that’s why I tend to drink<br>at night,” - Gedric</p>
    <p>“Two beer or not two<br>beer,” - Shakesbeer</p>
  </div>
  <div class="joke-column joke-column--jokes">
    <p>Why do frogs taste like<br>beer? Because of all the<br>hops</p>
    <p>What does Santa Claus<br>drink? A polar beer<br>Why do we like beer?<br>Coz you can’t drink bacon</p>
    <p>Fat? Nah, beer makes you<br>lean…<br>…against walls,<br>doors…hotties</p>
    <p>What's a beer’s favourite<br>language?<br>Hebrew</p>
  </div>
  <div class="tagline">GEDRIC’S LAGER IS LIFE’S BEER NECESSITY</div>
</section>

<section class="label label--three">
  <div class="paisley-field" role="img" aria-label="Paisley pattern background"></div>
  <div class="brand-name">GEDRIC’S LAGER</div>
  <svg class="crest" viewBox="0 0 172 166">
    <defs><radialGradient id="portrait3" cx="50%" cy="40%" r="55%"><stop offset="0" stop-color="var(--portrait-light)"/><stop offset="1" stop-color="var(--portrait-dark)"/></radialGradient></defs>
    <path d="M4 4 H168 V118 L86 164 L4 118 Z" fill="var(--gold)"/>
    <path d="M14 10 H158 V112 L86 152 L14 112 Z" fill="var(--blue-bright)"/>
    <rect x="24" y="14" width="124" height="126" fill="url(#portrait3)" role="img" aria-label="Cartoon portrait of Gedric, smiling, with glasses"/>
  </svg>
  <div class="joke-column joke-column--sayings">
    <p>“A beer in each hand is a<br>balanced diet,” - Gedric</p>
    <p>“This beer tastes like I’m<br>not going to work<br>tomorrow,” - Gedric</p>
    <p>“Your beer isn’t<br>half-full…it’s halfway to<br>your next brew,” - Gedric</p>
    <p>“My doc says I shouldn’t<br>drink every day…<br>that’s why I tend to drink<br>at night,” - Gedric</p>
    <p>“Two beer or not two<br>beer,” - Shakesbeer</p>
  </div>
  <div class="joke-column joke-column--jokes">
    <p>Why do frogs taste like<br>beer? Because of all the<br>hops</p>
    <p>What does Santa Claus<br>drink? A polar beer<br>Why do we like beer?<br>Coz you can’t drink bacon</p>
    <p>Fat? Nah, beer makes you<br>lean…<br>…against walls,<br>doors…hotties</p>
    <p>What's a beer’s favourite<br>language?<br>Hebrew</p>
  </div>
  <div class="tagline">GEDRIC’S LAGER IS LIFE’S BEER NECESSITY</div>
</section>

</body>
</html>
```